Portal Panel Medic need professional looking business card printed on plastic, Commericial, Industri

We are family owned and operated garage door company in Indianapolis, Indiana. We sale service and install dock equipment, doors, operators. We are looking to expand our commercial/ industrial division. We also service all residential doors and operators. We are looking for a business that stands out of the crowd. We are committed to have the best customer service in the industry.

Target Market(s)

National and local general contractors, National/ Corpate service accounts,

Industry/Entity Type

Business Service

Contact Information for Business Card

To be printed on plastic stock

Font styles to use
Sans Serif

Colors
ffffff
f04a50
ec1f27

Requirements
Must have
• Name, website,email, phone number, position.
Nice to have
• A standout professional design

```html
<!DOCTYPE html>
<html lang="en">
<head>
<meta charset="utf-8">
<title>Portal Panel Medic — Business Card</title>
<link rel="stylesheet" href="https://fonts.googleapis.com/css2?family=Ubuntu:wght@300;400;700&display=swap">
<style>
  :root {
    --backdrop: #d4d4d4;
    --card-light: #e4e4e4;
    --card-red: #f04a50;
    --accent-red: #ec1f27;
    --ink-red: #e8454b;
    --ink-dark: #141414;
  }
  * { margin: 0; padding: 0; box-sizing: border-box; }
  html, body {
    width: 1200px;
    height: 900px;
    overflow: hidden;
  }
  body {
    background: var(--backdrop);
    font-family: "Ubuntu", sans-serif;
    display: flex;
    align-items: center;
    justify-content: center;
    gap: 60px;
  }
  .card {
    width: 520px;
    height: 297px;
    border-radius: 4px;
    position: relative;
    box-shadow: 0 6px 18px rgba(0, 0, 0, 0.18);
  }
  .card-front {
    background: var(--card-light);
    color: var(--ink-red);
    padding: 44px 48px;
  }
  .holder-name {
    font-weight: 400;
    font-size: 30px;
    letter-spacing: 0.14em;
    text-transform: uppercase;
    line-height: 1;
  }
  .holder-role {
    font-weight: 300;
    font-size: 17px;
    letter-spacing: 0.2em;
    text-transform: uppercase;
    margin-top: 8px;
  }
  .contact-list {
    list-style: none;
    margin-top: 30px;
    font-weight: 300;
    font-size: 14px;
    line-height: 1.55;
  }
  .card-back {
    background: var(--card-red);
    display: flex;
    align-items: center;
    justify-content: center;
  }
  .brand-name {
    font-weight: 700;
    font-size: 34px;
    color: var(--ink-dark);
    text-transform: uppercase;
    letter-spacing: 0.02em;
    line-height: 1;
    text-align: center;
  }
</style>
</head>
<body>
  <section class="card card-front">
    <h1 class="holder-name">Evan Marlow</h1>
    <p class="holder-role">Founder</p>
    <ul class="contact-list">
      <li class="contact-phone">+06 5127 48 90</li>
      <li class="contact-web">www.portalpanelmedic.com</li>
      <li class="contact-email">evan@portalpanelmedic.com</li>
    </ul>
  </section>

  <section class="card card-back">
    <p class="brand-name">Portal Panel Medic</p>
  </section>
</body>
</html>
```